Tidewell Provisions

Distributor of seasonings and spices to the restaurant industry.

Restaurant

Tidewell Provis
Dean Holcroft
TK Wandsley Distributor
317-640-8917
dean@tidewellprovisionsco.com

No minimum order
Gluten & MSG free soup bases

```html
<!DOCTYPE html>
<html lang="en">
<head>
<meta charset="UTF-8">
<title>Tidewell Provisions — Business Card</title>
<link rel="stylesheet" href="https://fonts.googleapis.com/css2?family=Open+Sans:wght@400;600;700&display=swap">
<style>
  :root {
    --backdrop: #ececec;
    --card-white: #ffffff;
    --band-dark: #1f1f1f;
    --band-mid: #4a4a4a;
    --band-light: #6b6b6b;
    --accent-red: #e0312b;
    --accent-yellow: #f2c230;
    --ink: #2b2b2b;
    --ink-soft: #3a3a3a;
    --band-text: #f4f4f4;
  }
  * { margin: 0; padding: 0; box-sizing: border-box; }
  html, body {
    width: 1200px;
    height: 1039px;
    overflow: hidden;
    background: var(--backdrop);
    font-family: "Open Sans", Arial, sans-serif;
  }
  .canvas {
    position: relative;
    width: 1200px;
    height: 1039px;
  }
  .business-card {
    position: absolute;
    left: 150px;
    top: 262px;
    width: 900px;
    height: 514px;
    background: var(--card-white);
    box-shadow: 0 6px 24px rgba(0,0,0,0.18);
    overflow: hidden;
  }
  .card-band {
    position: absolute;
    inset: 0;
    width: 900px;
    height: 514px;
  }
  .brand-name {
    position: absolute;
    left: 372px;
    top: 70px;
    font-weight: 600;
    font-size: 56px;
    line-height: 1.05;
    color: var(--ink);
  }
  .brand-name .line-two { display: block; padding-left: 70px; }
  .holder {
    position: absolute;
    left: 50px;
    top: 158px;
    color: var(--ink);
  }
  .holder-name {
    font-size: 30px;
    font-weight: 400;
    line-height: 1.1;
  }
  .holder-title {
    font-size: 13px;
    font-weight: 700;
    color: var(--ink-soft);
    margin-top: 2px;
  }
  .contact {
    position: absolute;
    right: 40px;
    bottom: 28px;
    text-align: right;
    color: var(--band-text);
    font-style: normal;
    font-weight: 600;
    font-size: 20px;
    letter-spacing: 0.8px;
    line-height: 1.75;
  }
</style>
</head>
<body>
<main class="canvas">
  <section class="business-card">
    <svg class="card-band" viewBox="0 0 900 514" aria-hidden="true">
      <defs>
        <linearGradient id="bandShade" x1="0" y1="0" x2="1" y2="0">
          <stop offset="0" stop-color="#1f1f1f"/>
          <stop offset="0.55" stop-color="#4a4a4a"/>
          <stop offset="1" stop-color="#6b6b6b"/>
        </linearGradient>
      </defs>
      <path d="M0 232 C 250 330, 600 450, 900 300 L900 514 L0 514 Z" fill="url(#bandShade)"/>
      <path d="M0 228 C 250 326, 600 446, 900 296" fill="none" stroke="#f2c230" stroke-width="2"/>
      <path d="M0 231 C 250 329, 600 449, 900 299" fill="none" stroke="#e0312b" stroke-width="2"/>
    </svg>

    <h1 class="brand-name">Tidewell<span class="line-two">Provisions</span></h1>

    <div class="holder">
      <p class="holder-name">Dean Holcroft</p>
      <p class="holder-title">Distributor</p>
    </div>

    <address class="contact">
      <p>E: dean@tidewellprovisionsco.com</p>
      <p>P: 317-640-8917 / No minimum order / Gluten &amp; MSG free soup bases</p>
    </address>
  </section>
</main>
</body>
</html>
```